Harborne Cellarbook: the premier wine registry - (need business cards)

We have a logo designed, and now we need business cards for our 3 founders. Harborne Cellarbook is the premier wine registry for weddings. I am envisioning the wine glass with the heart in it as our signature symbol. (FYI- on the red background file, only use the part that has the red background; the brown colors are not relevant)

```html
<!DOCTYPE html>
<html lang="en">
<head>
<meta charset="utf-8">
<title>Harborne Cellarbook — Business Cards</title>
<link rel="stylesheet" href="https://fonts.googleapis.com/css2?family=Montserrat:wght@400;500;600&display=swap">
<style>
  :root {
    --backdrop: #262527;
    --wine: #96264e;
    --paper: #ffffff;
    --silver: #c9c9c9;
    --ink-grey: #a6a6a6;
    --card-radius: 22px;
  }
  * { box-sizing: border-box; margin: 0; padding: 0; }
  html, body { width: 1200px; height: 880px; overflow: hidden; background: var(--backdrop); }
  body { position: relative; font-family: "Montserrat", Arial, sans-serif; }

  .card {
    position: absolute;
    width: 560px;
    height: 320px;
    border-radius: var(--card-radius);
    box-shadow: 0 14px 30px rgba(0,0,0,0.45);
  }
  .card--front { left: 120px; top: 90px; background: var(--wine); display: flex; align-items: center; justify-content: center; }
  .card--back { left: 520px; top: 470px; background: var(--paper); display: flex; align-items: center; }

  .brand { display: flex; align-items: center; gap: 12px; font-weight: 500; letter-spacing: 0.04em; }
  .brand__dot { width: 16px; height: 16px; border-radius: 50%; flex: none; }
  .card--front .brand { color: var(--silver); font-size: 30px; }
  .card--front .brand__dot { background: var(--silver); }

  .card--back .brand { color: var(--wine); font-size: 21px; width: 290px; justify-content: center; margin-top: 60px; }
  .card--back .brand__dot { background: var(--wine); width: 13px; height: 13px; }

  .divider { width: 1.5px; height: 120px; background: var(--wine); margin: 0 26px 0 4px; }

  .contact { color: var(--ink-grey); font-size: 12.5px; line-height: 1.45; }
  .contact__name { font-size: 17px; font-weight: 600; letter-spacing: 0.02em; color: var(--ink-grey); }
  .contact__first { color: var(--wine); }
  .contact__role { margin-bottom: 8px; }
  .contact__row { display: flex; align-items: center; gap: 8px; margin-top: 4px; }
  .contact__icon { width: 18px; height: 18px; flex: none; }
</style>
</head>
<body>
  <section class="card card--front" aria-label="Card front">
    <div class="brand"><span class="brand__dot"></span>Harborne Cellarbook</div>
  </section>

  <section class="card card--back" aria-label="Card back">
    <div class="brand"><span class="brand__dot"></span>Harborne Cellarbook</div>
    <div class="divider"></div>
    <div class="contact">
      <p class="contact__name"><span class="contact__first">EVAN</span> MARLOW</p>
      <p class="contact__role">Founder</p>
      <p>4120 W. Vine Ct.</p>
      <p>Cedar Lane, Oregon 97000</p>
      <p class="contact__row">
        <svg class="contact__icon" viewBox="0 0 18 18" aria-hidden="true">
          <circle cx="9" cy="9" r="9" fill="#cfcfcf"/>
          <path d="M5 7.5c0-1.2 1.8-2 4-2s4 .8 4 2l-1.4.6-.6-1.3H7l-.6 1.3z M6.5 9h5l.8 3.5H5.7z" fill="#96264e"/>
        </svg>
        503-555-0142
      </p>
      <p class="contact__row">
        <svg class="contact__icon" viewBox="0 0 18 18" aria-hidden="true">
          <circle cx="9" cy="9" r="9" fill="#cfcfcf"/>
          <rect x="4.5" y="6" width="9" height="6.2" rx="0.8" fill="#96264e"/>
          <path d="M4.8 6.4 9 9.6l4.2-3.2" fill="none" stroke="#fff" stroke-width="0.9"/>
        </svg>
        hello@cellarbook.example
      </p>
    </div>
  </section>
</body>
</html>
```